complete redesign of VitaPlate.com

VITAPLATE.COM
MAIN MANU

We need it cut into HTML / Wordpress Friendly.... Our developer will handle all the WP / PHP coding, but we need it placed into HTML format so he can put into wordpress.

Please see the old vitaplate.com by visiting www.vitaplate.com... we want something completely different, but... just use this site for reference as to audience, theme, etc... we want something where it is science meets diet in helping fight cancer :)

WE NEED SOMETHING MORE MODERN AND MEDICAL IN TERMS OF DESIGN

See below:

1 CANCER NEWS
2 NUTRITION DIAGNOSTICS
3 DIET STEPS
4 DIET SUPPLEMENTS IN CANCER 
5 DICTIONARY OF MARKINGS ON FOOD
6 MERIVOLA VIDEOS
7 YOUR INDIVIDUAL DIET - SUBSCRIPTION

a. CANCER NEWS - latest articles relating to cancer prevention research treatments

b. NUTRITION DIAGNOSTICS -  description of the research that must be done to determine the degree of malnutrition of the body a place on the charts
pictures, etc.

c. DIET STEPS 
(sub menu - @)
¥ prevention of oncological - @
¥ diet chemotherapy - @
¥ diet in radiotherapy - @
¥ hormonal diet - @
¥ diet during convalescence - @

d. DIET SUPPLEMENTS IN CANCER - articles describing various supplements summary tables, etc.

e. DICTIONARY OF MARKINGS ON FOOD - composition, translation of labels on food, itd.

f. MERIVOLA VIDEOS 
(sub menu - @)
¥ healthy cooking - @
¥ meal preparation - @
¥ storage of food - @
¥ eco food - @
¥ rehabilitation - @
¥ yoga - @
¥ exercises - @
¥ psycho-oncology training - @
¥ music therapy - @

g. YOUR INDIVIDUAL DIET -  individual personalized diet for subscribing. We
add this point by developing a system of diet.

After 3 months, we will add special individual programs that mix diet, exercise and psychological lectures

Industry/Entity Type

Medical

Logo Text

Vita Plate / VitaPlate.com

Number of Pages Required

5+ page

Font styles to use
Sans Serif

Colors
ec1f27
9bcb3c
ffffff

Requirements
Must have
• HTML/CSS

```html
<!DOCTYPE html>
<html lang="en">
<head>
<meta charset="utf-8">
<title>Vita Plate</title>
<link rel="stylesheet" href="https://fonts.googleapis.com/css2?family=Open+Sans:wght@400;600;700&family=Roboto+Slab:wght@400;700&display=swap">
<style>
:root{
  --green:#9bcb3c;
  --green-dark:#86b52c;
  --green-soft:#eef6dc;
  --red:#ec1f27;
  --white:#ffffff;
  --ink:#222222;
  --text:#555555;
  --muted:#8a8a8a;
  --line:#d9d9d9;
  --grey-bg:#f0f0f0;
  --dark:#2a2a2a;
  --footer:#262626;
}
*{box-sizing:border-box;margin:0;padding:0}
html,body{width:1200px;height:5128px;overflow:hidden}
body{font-family:"Open Sans",Arial,sans-serif;color:var(--text);background:var(--white);position:relative}
.abs{position:absolute}
.section-title{position:absolute;left:0;width:1200px;text-align:center;font-size:38px;font-weight:600;color:var(--ink);letter-spacing:.5px}
.section-sub{position:absolute;left:0;width:1200px;text-align:center;font-size:15px;color:var(--text)}
.photo{position:absolute}

/* hero */
.hero{position:absolute;left:0;top:0;width:1200px;height:660px;
  background:linear-gradient(100deg,#3a2f27 0%,#4a3c31 45%,#4e5a2c 70%,#6b8a2e 85%,#8a3a25 100%)}
.nav{position:absolute;top:20px;left:0;width:1200px;display:flex;justify-content:center;gap:38px}
.nav a{color:var(--white);text-decoration:none;font-size:14px;font-weight:600;letter-spacing:.5px}
.nav a.active{color:var(--green)}
.hero-ribbon{left:188px;top:154px;width:274px;height:461px;background:linear-gradient(160deg,#f07ab0,#d8447f);border-radius:40px}
.brand-name{position:absolute;left:434px;top:300px;font-size:36px;font-weight:700;color:var(--white)}

/* overview */
.post-icon{position:absolute;border:2px solid var(--line);display:flex;align-items:center;justify-content:center;background:var(--white)}
.post-title{position:absolute;font-family:"Roboto Slab",Georgia,serif;font-size:18px;font-weight:700;color:var(--ink);text-transform:uppercase}
.post-meta{position:absolute;font-size:12px;color:var(--muted)}
.post-body{position:absolute;font-size:14px;line-height:21px;color:var(--text)}
.btn{position:absolute;display:flex;align-items:center;justify-content:center;font-size:15px;text-transform:uppercase}
.btn-green{background:var(--green-soft);border:2px solid var(--green);color:var(--green-dark)}
.btn-grey{background:#e6e6e6;border:2px solid #9a9a9a;color:var(--ink)}
.video-tile{left:622px;top:855px;width:500px;height:315px;background:linear-gradient(135deg,#b6d86a,#8fc03a 60%,#7aa92c)}
.video-tile .label{position:absolute;left:0;top:140px;width:500px;text-align:center;color:var(--white);font-family:"Roboto Slab",Georgia,serif;font-size:22px}
.video-tile .sub{position:absolute;left:150px;top:178px;width:200px;text-align:center;color:var(--white);font-size:12px;line-height:16px}
.quote{position:absolute;left:144px;top:1214px;width:352px;height:222px;border:3px double var(--green);text-align:center;padding:40px 28px}
.quote h3{font-family:"Roboto Slab",Georgia,serif;font-weight:400;font-size:22px;color:var(--ink);margin-bottom:18px}
.quote p{font-family:"Roboto Slab",Georgia,serif;font-size:19px;line-height:27px;color:var(--ink)}

/* diagnostics */
.diagnostics{position:absolute;left:0;top:1870px;width:1200px;height:735px;background:linear-gradient(120deg,#2f3a24,#4b5238 40%,#3a4430 70%,#2b3322)}
.food-dot{position:absolute;width:96px;height:96px;border-radius:50%;background:var(--white)}

/* steps */
.steps{position:absolute;left:0;top:2605px;width:1200px;height:729px;background:var(--grey-bg)}
.card{position:absolute;top:225px;width:335px;height:380px;background:var(--white);border-radius:10px;text-align:center}
.card.featured{background:var(--green)}
.card h4{position:absolute;top:112px;left:0;width:100%;font-family:"Roboto Slab",Georgia,serif;font-weight:400;font-size:22px;color:var(--ink)}
.card.featured h4{color:var(--white)}
.card ul{position:absolute;top:160px;left:40px;right:30px;text-align:left;list-style:none;font-size:13px;line-height:24px;color:var(--text)}
.card.featured ul{color:var(--white)}
.card ul li::before{content:"• "}
.card .btn{top:300px;left:50%;margin-left:-85px;width:170px;height:48px}
.card .btn-light{background:#f6f6f6;border:2px solid #bdbdbd;color:var(--ink)}
.step-badge{position:absolute;left:50%;top:-30px;margin-left:-55px;width:110px;height:110px;border-radius:50%;display:flex;align-items:center;justify-content:center}
.dots{position:absolute;top:640px;left:570px;display:flex;gap:10px}
.dots span{width:16px;height:16px;border-radius:50%;border:2px solid var(--green)}
.dots span.on{background:var(--green)}

/* feature tiles */
.feature-caption{position:absolute;bottom:10px;left:0;width:600px;height:70px;background:rgba(0,0,0,.55);color:var(--white);font-family:"Roboto Slab",Georgia,serif;font-size:20px;letter-spacing:1px;display:flex;align-items:center;justify-content:center}

/* videos */
.video-list{position:absolute;left:75px;top:3898px;width:311px;height:377px;background:#eeeeee}
.video-list .bar{position:absolute;left:0;width:311px;height:28px;background:var(--green);display:flex;align-items:center;justify-content:center}
.video-item{position:absolute;left:14px;width:290px;height:92px}
.video-item .thumb{position:absolute;left:0;top:8px;width:108px;height:76px}
.video-item .t{position:absolute;left:124px;top:10px;width:160px;font-size:14px;font-weight:700;color:var(--ink);line-height:20px}
.video-item .m{position:absolute;left:124px;top:58px;font-size:11px;color:var(--muted)}
.tabs{position:absolute;left:113px;top:4320px;width:980px;display:flex;justify-content:space-between;font-size:14px;color:var(--ink)}
.tabs span.on{border-bottom:2px solid var(--ink);padding-bottom:4px}

/* subscribe */
.subscribe{position:absolute;left:0;top:4417px;width:1200px;height:421px;background:linear-gradient(90deg,#3a3a3a,#4a4a48 50%,#3c3c3a)}
.subscribe h3{position:absolute;left:0;width:1200px;text-align:center;font-family:"Roboto Slab",Georgia,serif;font-weight:400;color:var(--white)}
.email{position:absolute;left:386px;top:213px;width:424px;height:55px;background:var(--green);border-radius:3px;color:var(--white);font-size:15px;padding:16px 18px}
.email .go{position:absolute;right:6px;top:6px;width:52px;height:43px;background:#b5dc67;display:flex;align-items:center;justify-content:center}

/* footer */
.footer{position:absolute;left:0;top:4838px;width:1200px;height:290px;background:var(--footer);color:#cfcfcf}
.footer h5{position:absolute;top:34px;font-size:17px;font-weight:600;color:var(--white)}
.footer .links{position:absolute;left:75px;top:72px;list-style:none;font-size:13px;line-height:28px}
.footer .links li.on{color:var(--green)}
.social{position:absolute;left:345px;top:80px;display:flex;gap:14px}
.social span{width:20px;height:20px;border-radius:50%;background:var(--green)}
.tweet{position:absolute;left:619px;width:260px;font-size:12px;line-height:17px}
.tweet .bird{position:absolute;left:0;top:2px;width:28px;height:28px;border-radius:50%;background:#bdbdbd}
.tweet p{margin-left:42px}
.tweet .ago{color:var(--green)}
.foot-brand{position:absolute;left:906px;top:112px;font-size:26px;font-weight:700;color:var(--white)}
.copy{position:absolute;left:0;bottom:0;width:1200px;height:50px;border-top:1px solid #3a3a3a;text-align:center;line-height:50px;font-size:13px;color:var(--green)}
</style>
</head>
<body>

<header class="hero">
  <nav class="nav">
    <a class="active" href="#">HOME</a><a href="#">ABOUT</a><a href="#">RECIPES</a><a href="#">SCIENTIFIC APPROUCH</a><a href="#">OUR TEAM</a><a href="#">BLOG</a><a href="#">CONTACT</a>
  </nav>
  <div class="photo hero-ribbon" role="img" aria-label="Pink awareness ribbon on dark wood with fresh vegetables"></div>
  <div class="brand-name">Vita Plate</div>
</header>

<section class="overview">
  <h2 class="section-title" style="top:712px">Overview</h2>
  <p class="section-sub" style="top:795px">Latest Articles relating to Cancer Prevention Research Treatments</p>

  <div class="post-icon" style="left:75px;top:848px;width:96px;height:116px">
    <svg width="40" height="40" viewBox="0 0 40 40"><rect x="6" y="4" width="28" height="32" fill="none" stroke="#9bcb3c" stroke-width="3"/><line x1="6" y1="14" x2="34" y2="14" stroke="#9bcb3c" stroke-width="2"/><line x1="6" y1="26" x2="34" y2="26" stroke="#9bcb3c" stroke-width="2"/><line x1="13" y1="4" x2="13" y2="36" stroke="#9bcb3c" stroke-width="2"/><line x1="27" y1="4" x2="27" y2="36" stroke="#9bcb3c" stroke-width="2"/></svg>
  </div>
  <div class="post-title" style="left:205px;top:894px">Anti Cancer Diet Flush</div>
  <div class="post-meta" style="left:205px;top:922px">August 6, 2015 - By Lena Marsh</div>
  <p class="post-body" style="left:75px;top:990px;width:505px">Here is another post - this is just a test Here is another post - this is just a test Here is another post - this is just a test Here is another post - this is just a test Here is another post - this is just a test Here is another post - this is just a test Here is another post - this is just a test Here is anot...</p>
  <div class="btn btn-green" style="left:75px;top:1115px;width:171px;height:55px">Read More</div>

  <div class="photo video-tile" role="img" aria-label="Green capsules video thumbnail">
    <svg class="abs" style="left:232px;top:96px" width="36" height="36" viewBox="0 0 40 40"><rect x="6" y="4" width="28" height="32" fill="none" stroke="#fff" stroke-width="3"/><line x1="6" y1="14" x2="34" y2="14" stroke="#fff" stroke-width="2"/><line x1="6" y1="26" x2="34" y2="26" stroke="#fff" stroke-width="2"/></svg>
    <div class="label">VIDEO IN POP UP</div>
    <div class="sub">Lorem Ipsum is simply dummy text of the printing and typesetting industry.</div>
    <svg class="abs" style="left:232px;top:222px" width="36" height="12"><circle cx="6" cy="6" r="5" fill="#fff"/><circle cx="28" cy="6" r="5" fill="none" stroke="#fff" stroke-width="2"/></svg>
  </div>

  <div class="quote">
    <h3>You Are What You Eat.</h3>
    <p>Lorem Ipsum is simply dummy text of the printing and typesetting industry.</p>
  </div>

  <div class="post-icon" style="left:650px;top:1224px;width:102px;height:116px">
    <svg width="40" height="40" viewBox="0 0 40 40"><rect x="6" y="4" width="28" height="32" fill="none" stroke="#9bcb3c" stroke-width="3"/><line x1="6" y1="14" x2="34" y2="14" stroke="#9bcb3c" stroke-width="2"/><line x1="6" y1="26" x2="34" y2="26" stroke="#9bcb3c" stroke-width="2"/><line x1="13" y1="4" x2="13" y2="36" stroke="#9bcb3c" stroke-width="2"/><line x1="27" y1="4" x2="27" y2="36" stroke="#9bcb3c" stroke-width="2"/></svg>
  </div>
  <div class="post-title" style="left:780px;top:1270px">Anti Cancer Jucing</div>
  <div class="post-meta" style="left:780px;top:1298px">August 6, 2015 - By Lena Marsh</div>
  <p class="post-body" style="left:650px;top:1362px;width:478px">and here we have yet another post and here we have yet another post and here we have yet another post and here we have yet another post and here we have yet another post</p>

  <div class="photo" style="left:75px;top:1491px;width:506px;height:314px;background:linear-gradient(135deg,#e8e4dc,#cfc7ba 60%,#b3a897)" role="img" aria-label="Video still of a man speaking to camera"></div>

  <div class="post-icon" style="left:622px;top:1504px;width:103px;height:103px">
    <svg width="40" height="40" viewBox="0 0 40 40"><path d="M8 32 L10 24 L26 8 L32 14 L16 30 Z" fill="none" stroke="#9bcb3c" stroke-width="3" stroke-linejoin="round"/><line x1="8" y1="36" x2="32" y2="36" stroke="#9bcb3c" stroke-width="2"/></svg>
  </div>
  <div class="post-title" style="left:745px;top:1533px">Stop Cancer In Its Tracks</div>
  <div class="post-meta" style="left:745px;top:1561px">August 6, 2015 - By Lena Marsh</div>
  <p class="post-body" style="left:622px;top:1626px;width:506px">This is where we write about the next video... A small write up goes here :) This is where we write about the next video... A small write up goes here :) This is where we write about the next video... A small write up goes here :) This is where we write about the next...</p>
  <div class="btn btn-grey" style="left:622px;top:1757px;width:168px;height:48px">Read More</div>
</section>

<section class="diagnostics" role="img" aria-label="Fresh green vegetables and herbs on a dark table">
  <h2 class="section-title" style="top:58px;color:#fff;font-weight:400;letter-spacing:2px">NUTRITION DIAGNOSTICS</h2>
  <p class="section-sub" style="top:118px;color:#fff">description of the research</p>

  <div class="abs" style="left:118px;top:168px;color:var(--green);font-size:15px;font-weight:700">OILY FISH</div>
  <div class="abs" style="left:92px;top:192px;width:140px;color:#fff;font-size:11px;line-height:15px;text-align:center">Lorem ipsum is simply dummy text of the</div>
  <svg class="abs" style="left:215px;top:175px" width="200" height="10"><line x1="0" y1="5" x2="200" y2="5" stroke="#fff" stroke-width="1.5"/><circle cx="5" cy="5" r="4" fill="#fff"/></svg>

  <div class="abs" style="left:411px;top:184px;width:108px;height:108px;border-radius:50%;background:radial-gradient(#f28a4a,#e0622a);border:5px solid #fff" role="img" aria-label="Salmon fillet"></div>
  <div class="food-dot" style="left:561px;top:192px"></div>
  <div class="food-dot" style="left:687px;top:192px"></div>
  <div class="food-dot" style="left:284px;top:243px"></div>
  <div class="food-dot" style="left:821px;top:243px"></div>
  <div class="food-dot" style="left:232px;top:373px"></div>
  <div class="food-dot" style="left:862px;top:373px"></div>
  <div class="food-dot" style="left:284px;top:510px"></div>
  <div class="food-dot" style="left:821px;top:510px"></div>
  <div class="food-dot" style="left:417px;top:562px"></div>
  <div class="food-dot" style="left:561px;top:562px"></div>
  <div class="food-dot" style="left:687px;top:562px"></div>

  <div class="abs" style="left:400px;top:330px;width:410px;height:190px;background:linear-gradient(90deg,#c94a3a,#8fbf3a);border-radius:6px;opacity:.85" role="img" aria-label="Hand lettered 'Your Nutrition' made of vegetables"></div>
</section>

<section class="steps">
  <h2 class="section-title" style="top:40px">DIET STEPS</h2>
  <p class="section-sub" style="top:120px">Description of the research</p>

  <div class="card" style="left:79px">
    <div class="step-badge" style="background:#fff;border:2px solid #e2e2e2">
      <svg width="44" height="44" viewBox="0 0 44 44"><circle cx="18" cy="18" r="11" fill="none" stroke="#444" stroke-width="4"/><line x1="26" y1="26" x2="38" y2="38" stroke="#444" stroke-width="5" stroke-linecap="round"/></svg>
    </div>
    <h4>Prevention of Oncological</h4>
    <ul><li>Lorem Ipsum is simply dummy text of</li><li>the printing and typesetting industry.</li><li>Lorem Ipsum has been the industry's</li><li>standard dummy text ever</li></ul>
    <div class="btn btn-light">Read More</div>
  </div>

  <div class="card featured" style="left:434px;top:215px;height:395px">
    <div class="step-badge" style="background:var(--green);border:6px solid #fff">
      <svg width="48" height="48" viewBox="0 0 48 48"><circle cx="24" cy="24" r="7" fill="none" stroke="#fff" stroke-width="4"/><circle cx="24" cy="11" r="6" fill="#fff"/><circle cx="13" cy="31" r="6" fill="#fff"/><circle cx="35" cy="31" r="6" fill="#fff"/></svg>
    </div>
    <h4>Diet Chemotherapy</h4>
    <ul><li>Lorem Ipsum is simply dummy text of</li><li>the printing and typesetting industry.</li><li>Lorem Ipsum has been the industry's</li><li>standard dummy text ever</li></ul>
    <div class="btn" style="background:var(--green);border:2px solid #fff;color:#fff">Read More</div>
  </div>

  <div class="card" style="left:793px;width:329px">
    <div class="step-badge" style="background:#fff;border:2px solid #e2e2e2">
      <svg width="44" height="44" viewBox="0 0 44 44"><circle cx="18" cy="18" r="11" fill="none" stroke="#444" stroke-width="4"/><line x1="26" y1="26" x2="38" y2="38" stroke="#444" stroke-width="5" stroke-linecap="round"/></svg>
    </div>
    <h4>Diet in Radiotherapy</h4>
    <ul><li>Lorem Ipsum is simply dummy text of</li><li>the printing and typesetting industry.</li><li>Lorem Ipsum has been the industry's</li><li>standard dummy text ever</li></ul>
    <div class="btn btn-light">Read More</div>
  </div>

  <div class="dots"><span class="on"></span><span></span></div>
</section>

<section class="features">
  <div class="photo" style="left:0;top:3334px;width:600px;height:420px;background:linear-gradient(135deg,#5a6a2a,#b08a3a 45%,#7a5a2a 75%,#3a3a22)" role="img" aria-label="Bowl of assorted dietary supplement capsules">
    <div class="feature-caption">DIET SUPPLEMENTS IN CANCER</div>
  </div>
  <div class="photo" style="left:600px;top:3334px;width:600px;height:420px;background:linear-gradient(135deg,#2e2a26,#6a3a2a 40%,#e0704a 65%,#3a3530)" role="img" aria-label="Raw salmon fillets with herbs and tomatoes">
    <div class="feature-caption">DICTIONARY OF MARKINGS ON FOOD</div>
  </div>
</section>

<section class="videos">
  <h2 class="section-title" style="top:3806px;font-weight:400;letter-spacing:1px">MERIVOLA VIDEOS</h2>

  <div class="video-list">
    <div class="bar" style="top:0"><svg width="16" height="10"><path d="M2 8 L8 2 L14 8" fill="none" stroke="#fff" stroke-width="2.5"/></svg></div>
    <div class="video-item" style="top:38px;background:#fff">
      <div class="thumb" style="background:linear-gradient(135deg,#c8402e,#e8c47a)" role="img" aria-label="Healthy meal thumbnail"></div>
      <div class="t">Lorem Ipsum is simply a dummy</div><div class="m">Posted: 2 months ago</div>
    </div>
    <div class="video-item" style="top:140px">
      <div class="thumb" style="background:linear-gradient(135deg,#d8e4c8,#7aa94a)" role="img" aria-label="Salad preparation thumbnail"></div>
      <div class="t">Lorem Ipsum is simply a dummy</div><div class="m">Posted: 3 months ago</div>
    </div>
    <div class="video-item" style="top:242px">
      <div class="thumb" style="background:linear-gradient(135deg,#e8eef0,#9ac0c8)" role="img" aria-label="Exercise thumbnail"></div>
      <div class="t">Lorem Ipsum is simply a dummy</div><div class="m">Posted: 5 months ago</div>
    </div>
    <div class="bar" style="bottom:0"><svg width="16" height="10"><path d="M2 2 L8 8 L14 2" fill="none" stroke="#fff" stroke-width="2.5"/></svg></div>
  </div>

  <div class="photo" style="left:465px;top:3908px;width:602px;height:367px;background:linear-gradient(135deg,#e6e2d8,#cfc6b2 50%,#a8a08a)" role="img" aria-label="Video of a woman preparing vegetables in a kitchen">
    <svg class="abs" style="left:261px;top:143px" width="80" height="80" viewBox="0 0 80 80"><circle cx="40" cy="40" r="38" fill="rgba(0,0,0,.45)"/><path d="M32 25 L56 40 L32 55 Z" fill="#fff"/></svg>
  </div>

  <div class="tabs">
    <span class="on">Healthy Cooking</span><span>Meal Preparation</span><span>Storage of Food</span><span>Eco Food</span><span>Rehabilitation</span><span>Yoga</span><span>Exercises</span><span>Training</span><span>Music</span>
  </div>
</section>

<section class="subscribe">
  <div class="photo" style="left:34px;top:131px;width:326px;height:274px;background:linear-gradient(160deg,#8a8a86,#d8d2c8 60%,#6a6a66);border-radius:4px" role="img" aria-label="Smiling woman pointing toward the signup form"></div>
  <h3 style="top:50px;font-size:28px">To Get Your</h3>
  <h3 style="top:92px;font-size:38px;letter-spacing:1px">OWN INDIVIDUAL DIET</h3>
  <h3 style="top:150px;font-size:20px">Subscribe us Here</h3>
  <div class="email">E-mail
    <div class="go"><svg width="26" height="18" viewBox="0 0 26 18"><rect x="1" y="1" width="24" height="16" fill="none" stroke="#fff" stroke-width="2"/><path d="M1 1 L13 10 L25 1" fill="none" stroke="#fff" stroke-width="2"/></svg></div>
  </div>
</section>

<footer class="footer">
  <h5 style="left:75px">Navigation</h5>
  <ul class="links"><li class="on">Terms &amp; Conditions</li><li>Disclaimer</li><li>Privacy Policy</li><li>FAQs</li></ul>

  <h5 style="left:345px">Social Media</h5>
  <div class="social"><span></span><span></span><span></span><span></span><span></span><span></span></div>

  <h5 style="left:619px">Recent Posts</h5>
  <div class="tweet" style="top:80px"><div class="bird"></div><p>@NoraVale @vitaplate<br>Thank you very much!<br><span class="ago">4 days ago</span></p></div>
  <div class="tweet" style="top:172px"><div class="bird"></div><p>@NoraVale @vitaplate<br>Thank you very much!<br><span class="ago">4 days ago</span></p></div>

  <div class="foot-brand">Vita Plate</div>

  <div class="copy">© VITA PLATE - 2015. All Rights Reserved.</div>
</footer>

</body>
</html>
```